Signal Post Hire Banner Ad Design Project

Hello Craft Throng,

We are looking for a banner ad that we can email to general contractors, and consulting firms in our service area to make them aware of our service.

We are an electrical contracting company based in Toronto, Ontario, Canada and one of divisions rents traffic light systems. We install our portable systems mainly in underground parking garages when construction restricts two way traffic to one lane. Our systems also get installed on ramps, and other areas that are under construction. Essentially, they allow phasing of big construction projects so the disruptions of traffic flow is kept to a minimal.
Our systems differ from other companies' rentals because our systems are cheaper, more reliable since they aren't wireless and they are LED (no bulbs burning out), we provide countdown lights that increase the effectiveness of the system and motorists' patience, and our systems adapt to rush hour traffic flow patterns at each site.
We have installed the systems at high profile locations throughout the city including The Marlow Quay Galleria, and Brinwick Mall.
We can provide job specific pricing or a monthly rate both of which include installation and removal.

I don't have very many good images of our systems but maybe you can photoshop our systems into another photo or a stock image might work as well.

More information on our systems can be found at www.fernholtvolt.example
Updates

Project Deadline Extended
Reason: Hi everyone, I am extending the deadline for submissions because I haven't had a proper chance to provide feedback to some of the designers who have submitted banner ads. I know it is frustrating when the deadline gets extended and I apologize. Thank you again and if I haven't provided feedback to you yet, please be patient because there have been some excellent designs that have been submitted so far. Dale

Project Deadline Extended
Reason: Still working with designers towards the right design.

Project Deadline Extended
Reason: I have been swamped with work and haven't been able to provide proper feedback to designers. Thanks for your patience, Dale

Industry/Entity Type

Construction

Requirements
Must have
• Fernholt Volt Logo

Focus on the fact that our systems are lower in price than our competitors or the fact that they are more cost effective.

Something that touches on the fact that our systems have countdown lights and adaptive control which increases traffic flow. This is a unique feature that no other company has.

```html
<!DOCTYPE html>
<html lang="en">
<head>
<meta charset="utf-8">
<title>Signal Post Hire – Banner</title>
<link href="https://fonts.googleapis.com/css2?family=Arimo:wght@400;700&display=swap" rel="stylesheet">
<style>
  :root {
    --ink: #050505;
    --white: #ffffff;
    --orange: #f08a1c;
    --orange-deep: #c9520c;
    --ember: #e5661a;
    --night: #1a0d08;
    --signal-yellow: #f2c81e;
    --signal-yellow-deep: #c99a0c;
    --trail-red: #c8241a;
    --gold: #e8c24a;
    --gold-deep: #b88a1e;
    --gold-text: #7a5a14;
  }
  * { margin: 0; padding: 0; box-sizing: border-box; }
  html, body { width: 1200px; height: 2400px; overflow: hidden; background: var(--white); }
  .banner {
    position: relative;
    width: 1200px; height: 2400px;
    overflow: hidden;
    font-family: "Arimo", Arial, sans-serif;
    background: var(--ink);
  }
  .masthead {
    position: absolute; left: 0; top: 0; width: 1200px; height: 300px;
    background: var(--ink);
    display: flex; align-items: center; justify-content: center;
  }
  .masthead__title {
    color: var(--white);
    font-size: 128px; font-weight: 400; letter-spacing: -1px;
    margin-top: -30px;
  }
  .accent-strip {
    position: absolute; left: 0; top: 300px; width: 1200px; height: 36px;
    background: linear-gradient(90deg, var(--orange-deep), var(--orange) 50%, var(--orange-deep));
  }
  .hero {
    position: absolute; left: 0; top: 336px; width: 1200px; height: 1884px;
    background: linear-gradient(180deg, #120806 0%, #1e0c08 35%, #6a2210 58%, var(--ember) 78%, var(--orange) 100%);
  }
  .light-trails {
    position: absolute; left: 280px; top: 520px; width: 1000px; height: 760px;
    border-radius: 50% 0 0 50%;
    background: linear-gradient(160deg, rgba(255,220,170,0.75) 0%, rgba(235,90,40,0.85) 35%, var(--trail-red) 65%, rgba(60,10,6,0.6) 100%);
    transform: rotate(-8deg);
  }
  .signal-head {
    position: absolute; left: 70px; top: 560px; width: 560px; height: 1120px;
    border-radius: 80px;
    background: linear-gradient(180deg, #ffe066 0%, var(--signal-yellow) 45%, var(--signal-yellow-deep) 100%);
    transform: rotate(-12deg);
    box-shadow: 0 30px 60px rgba(0,0,0,0.45);
  }
  .features {
    position: absolute; left: 120px; top: 360px;
    list-style: none;
    color: var(--white);
    font-size: 64px; line-height: 96px;
  }
  .features li { position: relative; padding-left: 88px; }
  .features li::before {
    content: ""; position: absolute; left: 0; top: 34px;
    width: 28px; height: 28px; border-radius: 50%;
    background: radial-gradient(circle at 35% 35%, #ffd27a, var(--orange) 60%, var(--orange-deep));
  }
  .decor { position: absolute; left: 0; top: 0; width: 1200px; height: 2400px; }
  .photo {
    position: absolute; border-radius: 50%;
    border: 12px solid var(--white);
  }
  .photo--site {
    left: 640px; top: 1160px; width: 480px; height: 480px;
    background: linear-gradient(180deg, #dfe6ea 0%, #c9cfcf 45%, #6f8a4a 75%, #8a8a84 100%);
  }
  .photo--city {
    left: 70px; top: 1610px; width: 460px; height: 460px;
    background: linear-gradient(180deg, #7fb3e0 0%, #a8cbe6 45%, #8a8e93 65%, #5d7a86 100%);
  }
  .seal {
    position: absolute; left: 660px; top: 1780px; width: 400px; height: 400px;
    border-radius: 50%;
    background: radial-gradient(circle at 40% 35%, #fbe38a, var(--gold) 55%, var(--gold-deep));
    box-shadow: 0 0 0 16px rgba(232,194,74,0.55);
    display: flex; align-items: center; justify-content: center;
    transform: rotate(-16deg);
  }
  .seal__text {
    color: var(--gold-text);
    font-size: 92px; font-weight: 700; line-height: 96px; text-align: center;
  }
  .footer {
    position: absolute; left: 0; top: 2220px; width: 1200px; height: 180px;
    background: var(--ink);
    display: flex; align-items: center; justify-content: center; gap: 28px;
  }
  .footer__mark { width: 76px; height: 76px; background: var(--orange); }
  .footer__name { color: var(--white); font-size: 80px; font-weight: 400; }
</style>
</head>
<body>
  <div class="banner">
    <header class="masthead">
      <h1 class="masthead__title">Signal Post Hire</h1>
    </header>
    <div class="accent-strip"></div>

    <div class="hero"></div>
    <div class="light-trails" role="img" aria-label="Photo of red and orange car light trails curving along a highway at night"></div>

    <svg class="decor" viewBox="0 0 1200 2400" aria-hidden="true">
      <g fill="none" stroke="rgba(255,210,150,0.35)" stroke-width="6">
        <circle cx="880" cy="1400" r="330"/>
        <circle cx="300" cy="1840" r="300"/>
        <circle cx="860" cy="1980" r="280"/>
      </g>
    </svg>

    <div class="signal-head" role="img" aria-label="Photo of a yellow LED traffic light with red, green countdown and green lamps"></div>

    <ul class="features">
      <li>Countdown Lights</li>
      <li>Adaptive Rush Hour Control</li>
    </ul>

    <div class="photo photo--site" role="img" aria-label="Photo of a portable traffic light installed at a construction site driveway"></div>
    <div class="photo photo--city" role="img" aria-label="Photo of a city skyline beside the lake"></div>

    <div class="seal">
      <span class="seal__text">Low<br>Price</span>
    </div>

    <footer class="footer">
      <span class="footer__mark"></span>
      <span class="footer__name">Fernholt Volt</span>
    </footer>
  </div>
</body>
</html>
```